Architecture firm needing a business card

We need a business card design for a new company based in the US called "Dorrance Architecture". Seeking minimalist designs that have a creativity/design feel but must be clean and professional. Please refer to the logo attached.

Target Market(s)

Real Estate Investors, Home Builders and Construction Firms.

Industry/Entity Type

Architecture

Contact Information for Business Card

Standard US size business cards. Would like to have some sort of graphic on the back side of the card - nothing that is too loud but something that may catch your attention. More or less grayscale colors that are in line with the logo colors (navy and greys essentially). Additional colors maybe accepted if blended properly (earthtones), but might be difficult to accomplish and maintain the clean/minimalist look.

Requirements
Must have
• Clean Lines
Nice to have
• some sort of graphics, would like to have something creative on the back side of the card
Should not have
• nothing too busy, cluttered or overwhelming.

```html
<!DOCTYPE html>
<html lang="en">
<head>
<meta charset="utf-8">
<title>Dorrance Architecture – Business Card</title>
<link rel="stylesheet" href="https://fonts.googleapis.com/css2?family=Source+Sans+3:wght@400;600&display=swap">
<style>
  :root {
    --backdrop: #282828;
    --card-white: #ffffff;
    --navy: #1f4268;
    --navy-text: #173a64;
    --grey-text: #555a60;
    --on-navy: #ffffff;
  }
  * { margin: 0; padding: 0; box-sizing: border-box; }
  html, body {
    width: 1200px; height: 900px; overflow: hidden;
    background: var(--backdrop);
    font-family: "Source Sans 3", sans-serif;
  }
  .stage { position: relative; width: 1200px; height: 900px; }
  .card {
    position: absolute; top: 306px;
    width: 439px; height: 271px; border-radius: 12px;
  }
  .card-front { left: 123px; background: var(--card-white); }
  .card-back  { left: 596px; background: var(--navy); }

  .brand { position: absolute; left: 64px; top: 32px; display: flex; align-items: center; gap: 14px; }
  .brand-square { width: 64px; height: 64px; background: var(--navy); }
  .brand-name {
    color: var(--navy-text); font-weight: 400; font-size: 27px;
    line-height: 1.05; letter-spacing: 2px; text-transform: uppercase;
  }

  .contact { position: absolute; left: 142px; top: 117px; color: var(--grey-text); font-size: 12.5px; line-height: 16px; }
  .person-name { color: var(--navy-text); font-weight: 600; font-size: 15.5px; line-height: 18px; }
  .person-role { margin-bottom: 14px; }
  .address { margin-bottom: 14px; }
  .contact-line { display: flex; align-items: center; gap: 5px; }
  .contact-line svg { width: 9px; height: 9px; fill: var(--navy-text); }

  .back-brand { position: absolute; left: 0; right: 0; top: 62px; display: flex; flex-direction: column; align-items: center; gap: 14px; }
  .back-square { width: 40px; height: 40px; background: var(--on-navy); }
  .back-name {
    color: var(--on-navy); font-weight: 400; font-size: 30px; line-height: 1.1;
    letter-spacing: 3px; text-transform: uppercase; text-align: center;
  }
  .website {
    position: absolute; left: 0; right: 0; top: 214px; text-align: center;
    color: var(--on-navy); font-size: 12.5px; letter-spacing: 1px;
  }
</style>
</head>
<body>
<main class="stage">
  <section class="card card-front">
    <div class="brand">
      <div class="brand-square"></div>
      <div class="brand-name">Dorrance<br>Architecture</div>
    </div>
    <div class="contact">
      <p class="person-name">Marcus Delaney</p>
      <p class="person-role">Managing Director</p>
      <p class="address">12345, Address Goes Here<br>Country Name, 123456.</p>
      <p class="contact-line">
        <svg viewBox="0 0 10 10" aria-hidden="true"><path d="M1 3c0-1 1-2 4-2s4 1 4 2v1H7V3H3v1H1zM2 5h6l1 4H1z"/></svg>
        044-987 654 321
      </p>
      <p class="contact-line">
        <svg viewBox="0 0 10 10" aria-hidden="true"><path d="M0 2h10v6H0zM1 3l4 3 4-3"/></svg>
        info@dorrancearch.com
      </p>
    </div>
  </section>

  <section class="card card-back">
    <div class="back-brand">
      <div class="back-square"></div>
      <div class="back-name">Dorrance<br>Architecture</div>
    </div>
    <p class="website">www.dorrancearch.com</p>
  </section>
</main>
</body>
</html>
```